Business Card Design Project

Need a business card that stands my education platform as a whole but

Target Market(s)

Parents, families, expats in the middle east.

Industry/Entity Type

Education

Contact Information for Business Card

www.brightlane.ae
www.homesteadhub.ae
www.littlenestcarers.ae

+971552419736
helena@brightlane.ae

Font styles to use
Serif

Requirements
Must have
• Logo's and contact details

```html
<!DOCTYPE html>
<html lang="en">
<head>
<meta charset="utf-8">
<title>Bright Lane – Business Card</title>
<link href="https://fonts.googleapis.com/css2?family=Open+Sans:wght@400;700&display=swap" rel="stylesheet">
<style>
  :root {
    --teal: #3f8ca6;
    --orange: #f0892c;
    --white: #ffffff;
    --backdrop: #cfcfcf;
    --ink: #3f8ca6;
  }
  * { box-sizing: border-box; margin: 0; padding: 0; }
  html, body { width: 1200px; height: 957px; overflow: hidden; }
  body {
    background: var(--backdrop);
    font-family: "Open Sans", Arial, sans-serif;
    display: flex;
    flex-direction: column;
    align-items: center;
    justify-content: center;
    gap: 56px;
  }
  .card {
    width: 620px;
    height: 354px;
    background: var(--white);
    box-shadow: 0 8px 24px rgba(0,0,0,0.18);
    position: relative;
    overflow: hidden;
  }
  /* Front */
  .card--front {
    display: flex;
    align-items: center;
    justify-content: center;
  }
  .brand {
    display: flex;
    align-items: center;
    gap: 14px;
    color: var(--ink);
    font-weight: 400;
    letter-spacing: 0.06em;
    text-transform: uppercase;
  }
  .brand__dot {
    width: 22px; height: 22px;
    border-radius: 50%;
    background: var(--orange);
  }
  .card--front .brand__name { font-size: 46px; }
  /* Back */
  .card--back { display: flex; }
  .contact-panel {
    width: 63%;
    height: 100%;
    background: var(--teal);
    color: var(--white);
    padding: 82px 0 0 44px;
    font-size: 21px;
    line-height: 1.5;
  }
  .contact-row { display: flex; }
  .contact-row__label { font-weight: 700; width: 86px; }
  .contact-row__values { display: flex; flex-direction: column; }
  .identity-panel {
    flex: 1;
    display: flex;
    flex-direction: column;
    align-items: center;
    justify-content: center;
    gap: 22px;
  }
  .identity-panel .brand { gap: 8px; }
  .identity-panel .brand__dot { width: 14px; height: 14px; }
  .identity-panel .brand__name { font-size: 22px; }
  .tagline {
    background: var(--teal);
    color: var(--white);
    font-weight: 700;
    font-size: 13px;
    line-height: 1.3;
    text-align: center;
    border-radius: 9px;
    padding: 6px 14px;
    width: 170px;
  }
</style>
</head>
<body>
  <section class="card card--front" aria-label="Card front">
    <div class="brand">
      <span class="brand__dot"></span>
      <span class="brand__name">Bright Lane</span>
    </div>
  </section>

  <section class="card card--back" aria-label="Card back">
    <div class="contact-panel">
      <div class="contact-row">
        <span class="contact-row__label">Web:</span>
        <span class="contact-row__values">
          <span>www.brightlane.ae</span>
          <span>www.homesteadhub.ae</span>
          <span>www.littlenestcarers.ae</span>
        </span>
      </div>
      <div class="contact-row">
        <span class="contact-row__label">Tell:</span>
        <span class="contact-row__values"><span>+971552419736</span></span>
      </div>
      <div class="contact-row">
        <span class="contact-row__label">Email:</span>
        <span class="contact-row__values"><span>helena@brightlane.ae</span></span>
      </div>
    </div>
    <div class="identity-panel">
      <div class="brand">
        <span class="brand__dot"></span>
        <span class="brand__name">Bright Lane</span>
      </div>
      <div class="tagline">Accelerated Learning Centre</div>
    </div>
  </section>
</body>
</html>
```